The KeoLum Fundraiser Brochure

We have tried a couple designers but they just took our ppt file and gave it back. This is the reason for us using this website. We are looking for something creative using the ppt file we have provided as an example. We have some other logo work we want done with a different name but looking to see what type of resulkts we get here first. Need a creative brochure for fundraising raising industry, working with elementary thru high schoolers. We would like to see designs that use "French Fry" font and "Leaky Ketchup" font where you see yellow text in the attached. See attached example. 81/2 X 11 Z-fold

Font styles to use
Sans Serif

Colors

Designer to choose colors to be used in the design.

Requirements
Must have
• KeoLum Logo "French Fry" font where you see yellow text; i.e. fundraiser, step 1
• KeoLum Logo "Leaky Ketchup" font where you see the red "keo"
Nice to have
• Keeping with the KeoLum theme

```html
<!DOCTYPE html>
<html lang="en">
<head>
<meta charset="utf-8">
<title>KeoLum Fundraiser Brochure</title>
<link href="https://fonts.googleapis.com/css2?family=Open+Sans:wght@400;600;700;800&display=swap" rel="stylesheet">
<style>
:root{
  --navy:#1c2a5c;
  --red:#d8232a;
  --yellow:#f6c21c;
  --grey:#eceff3;
  --ink:#2b2f3a;
  --white:#ffffff;
}
*{box-sizing:border-box;margin:0;padding:0}
html,body{width:696px;height:1200px;overflow:hidden;background:var(--white)}
body{font-family:"Open Sans",Arial,sans-serif;color:var(--ink);position:relative}
.spread{position:absolute;left:0;width:696px;display:flex;box-shadow:0 2px 6px rgba(0,0,0,.18);overflow:hidden}
.spread--outside{top:0;height:508px}
.spread--inside{top:592px;height:556px}
.panel{position:relative;width:232px;height:100%;overflow:hidden;background:var(--white)}
.panel + .panel{border-left:1px solid #dde1e8}
.caption{position:absolute;left:0;width:696px;text-align:center;font-size:15px;color:#555}
.caption--outside{top:534px}
.caption--inside{top:1168px}

.heading{font-family:"Open Sans",Arial,sans-serif;font-weight:800;color:var(--red);text-align:center;line-height:1.1;text-transform:uppercase}

/* outside left */
.charity-head{background:var(--navy);color:var(--yellow);font-weight:800;font-size:11px;line-height:1.3;text-align:center;padding:10px 12px;text-transform:uppercase}
.charity-list{display:grid;grid-template-columns:1fr 1fr;gap:18px 10px;padding:18px 14px}
.charity{display:flex;align-items:center;gap:6px;font-size:10px;font-weight:700;color:var(--navy);line-height:1.15}
.charity .dot{flex:0 0 16px;height:16px;border-radius:50%;background:var(--red)}
.charity:nth-child(even) .dot{background:var(--navy)}

/* marks */
.mark{display:flex;align-items:center;justify-content:center;gap:6px;font-weight:800;font-size:22px;color:var(--white)}
.mark .disc{width:18px;height:18px;border-radius:50%;background:var(--yellow)}
.left-mark{position:absolute;left:0;width:232px;bottom:36px}
.left-url{position:absolute;left:0;width:232px;bottom:14px;text-align:center;font-size:9px;color:var(--white)}

/* outside middle */
.rep-head{margin:14px 14px 0;background:var(--navy);color:var(--white);font-size:10px;font-weight:700;text-align:center;padding:8px 6px;text-transform:uppercase;line-height:1.3}
.rep-card{margin:0 14px;height:200px;border:2px solid var(--navy);border-top:none;background:var(--white)}
.center-mark{position:absolute;left:0;width:232px;top:302px}
.agency{position:absolute;top:392px;left:18px;right:18px;display:flex;align-items:center;gap:8px;font-size:12px;font-weight:800;color:var(--navy);line-height:1.1}
.agency .sq{width:22px;height:22px;background:var(--red);flex:0 0 22px}
.agency-addr{position:absolute;top:428px;left:18px;right:18px;font-size:7.5px;color:var(--white);line-height:1.4;text-align:center}

/* outside right */
.fund-title{padding-top:18px;font-size:26px}
.hand-phone{position:absolute;left:40px;top:92px;width:160px;height:210px;border-radius:18px;background:linear-gradient(160deg,#f2c9a5,#3a3f52 60%,#1d1f2a)}
.brand-grid{position:absolute;top:318px;left:14px;right:14px;display:grid;grid-template-columns:repeat(4,1fr);gap:8px}
.brand-grid span{height:20px;border-radius:4px;background:#e3e6ec}
.brand-grid span:nth-child(3n){background:#f4d6d6}
.brand-grid span:nth-child(4n){background:#fbe9b5}
.site-mark{position:absolute;bottom:20px;left:0;width:232px;text-align:center}
.site-url{font-size:9px;color:var(--white);margin-top:4px}

.band{position:absolute;left:0;bottom:0}

/* inside */
.step-title{padding-top:14px;font-size:26px}
.bar{margin:10px 14px 0;background:var(--navy);color:var(--white);font-weight:800;font-size:11px;text-align:center;padding:7px 6px;text-transform:uppercase;border-radius:3px;line-height:1.25}
.body-copy{margin:10px 14px 0;font-size:8.6px;line-height:1.5;color:#444}
.body-copy p + p{margin-top:8px}
.alert{margin:12px 14px 0;color:var(--red);font-weight:800;font-size:10px;text-align:center;line-height:1.35;text-transform:uppercase}
.url-bar{margin:8px 14px 0;background:var(--navy);color:var(--white);font-size:8px;font-weight:700;text-align:center;padding:6px 4px}
.screen{margin:10px 14px 0;height:104px;border:1px solid #c9ced8;background:linear-gradient(#dfe4ee 0 16px,#ffffff 16px)}
.call{margin:8px 14px 0;color:var(--red);font-weight:800;font-size:11px;text-align:center;line-height:1.3;text-transform:uppercase}

.panel--questions{background:var(--grey);padding:12px}
.question{background:var(--white);border-radius:10px;padding:9px 11px;font-size:10.5px;line-height:1.4;color:var(--navy);margin-bottom:9px;box-shadow:0 1px 2px rgba(0,0,0,.08)}
</style>
</head>
<body>

<section class="spread spread--outside">
  <div class="panel">
    <div class="charity-head">Some of the other charities that we are proud to support!</div>
    <div class="charity-list">
      <div class="charity"><span class="dot"></span>Harvest Table</div>
      <div class="charity"><span class="dot"></span>Bright Star Giving</div>
      <div class="charity"><span class="dot"></span>Global Hope</div>
      <div class="charity"><span class="dot"></span>Veterans Forward</div>
      <div class="charity"><span class="dot"></span>Bright Futures Fund</div>
      <div class="charity"><span class="dot"></span>Relief Alliance</div>
      <div class="charity"><span class="dot"></span>Shelter Circle</div>
      <div class="charity"><span class="dot"></span>Helping Hands Network</div>
    </div>
    <svg class="band" width="232" height="150" viewBox="0 0 232 150">
      <path d="M0 40 Q116 0 232 30 L232 150 L0 150Z" fill="var(--navy)"/>
      <path d="M0 40 Q116 0 232 30 L232 40 Q116 12 0 50Z" fill="var(--red)"/>
    </svg>
    <div class="mark left-mark"><span class="disc"></span>KeoLum</div>
    <div class="left-url">www.keolum.org</div>
  </div>

  <div class="panel">
    <div class="rep-head">Customer Satisfaction Representative</div>
    <div class="rep-card"></div>
    <svg class="band" width="232" height="260" viewBox="0 0 232 260">
      <path d="M0 60 Q116 -10 232 50 L232 260 L0 260Z" fill="var(--navy)"/>
      <path d="M0 60 Q116 -10 232 50 L232 62 Q116 4 0 72Z" fill="var(--red)"/>
      <rect x="10" y="140" width="212" height="40" rx="4" fill="var(--white)"/>
    </svg>
    <div class="mark center-mark"><span class="disc"></span>KeoLum</div>
    <div class="agency"><span class="sq"></span>Northstar 7<br>Marketing Group</div>
    <div class="agency-addr">2480 Maple Ridge Dr, Suite 14, Box 20<br>Fairview, Ohio 44100<br>www.northstar7.org</div>
  </div>

  <div class="panel">
    <div class="heading fund-title">keo Fundraiser</div>
    <div class="hand-phone" role="img" aria-label="Hand holding a smartphone showing the KeoLum fundraiser app"></div>
    <div class="brand-grid" role="img" aria-label="Partner restaurant badges">
      <span></span><span></span><span></span><span></span>
      <span></span><span></span><span></span><span></span>
      <span></span><span></span><span></span><span></span>
    </div>
    <svg class="band" width="232" height="110" viewBox="0 0 232 110">
      <path d="M0 50 Q116 10 232 30 L232 110 L0 110Z" fill="var(--navy)"/>
      <path d="M0 50 Q116 10 232 30 L232 40 Q116 22 0 60Z" fill="var(--red)"/>
    </svg>
    <div class="site-mark">
      <div class="mark"><span class="disc"></span>KeoLum</div>
      <div class="site-url">www.keolum.org</div>
    </div>
  </div>
</section>
<div class="caption caption--outside">Brochure Outside</div>

<section class="spread spread--inside">
  <div class="panel">
    <div class="heading step-title">keo Step 1</div>
    <div class="bar">Register to participate</div>
    <div class="body-copy">
      <p>If you have been involved in school fundraising with kids, you know how it goes: catalogs, order forms, cash in envelopes and boxes to deliver. We believe there is a far better way, one that lets families give to a good cause while enjoying meals they already love.</p>
      <p>The KeoLum app brings together many of your favorite local and national restaurants. Each of them offers generous rewards, and every purchase helps your school reach its goal without any selling door to door.</p>
    </div>
    <div class="alert">Each participant must register. Simply type this registration URL into your browser</div>
    <div class="url-bar">www.keolum.org/register</div>
    <svg class="band" width="232" height="60" viewBox="0 0 232 60">
      <path d="M0 20 Q116 0 232 16 L232 60 L0 60Z" fill="var(--navy)"/>
      <path d="M0 20 Q116 0 232 16 L232 24 Q116 10 0 28Z" fill="var(--red)"/>
    </svg>
  </div>

  <div class="panel">
    <div class="heading step-title">keo Step 2</div>
    <div class="bar">Let's pin, post, tag, text, or tweet</div>
    <div class="screen" role="img" aria-label="Screenshot of the KeoLum registration page"></div>
    <div class="heading step-title">keo Step 3</div>
    <div class="bar">Let's ask for some help</div>
    <div class="body-copy" style="text-align:center">You just sent them a post. Let's call and ask for some help to support your fundraiser.</div>
    <div class="call">Call 15 family members and friends</div>
    <svg class="band" width="232" height="90" viewBox="0 0 232 90">
      <path d="M0 40 Q116 0 232 36 L232 90 L0 90Z" fill="var(--navy)"/>
      <path d="M0 40 Q116 0 232 36 L232 46 Q116 14 0 50Z" fill="var(--red)"/>
    </svg>
  </div>

  <div class="panel panel--questions">
    <div class="question">Are you tired of fundraisers where you, the parent, do all the work?</div>
    <div class="question">Would you like a simplified process that doesn't require unsafe practices like door-to-door selling?</div>
    <div class="question">Would you like to eliminate the hassle of collecting money and delivering items?</div>
    <div class="question">Would you like a fundraising program that is 100% complete in one week?</div>
    <div class="question">Would you agree that family, friends, and parents are tired of buying items that have no purpose or value?</div>
    <div class="question">Do you agree that most family and friends would like to support a good cause?</div>
  </div>
</section>
<div class="caption caption--inside">Brochure Inside</div>

</body>
</html>
```